Financial Planning firm focused on serving women 55-65 yrs old needs stationary design

We are rebranding our financial planning firm and our target client is a 55-65 yr old women. We need a stationary design to go with our new logo.

Contact Information: Raymond Kessler, MS, CFP President Harlow Wealth Management 4820 Bramblewood Lane, Suite 317 Linden Bay, 00000 ray@harlowwealthmgmt.example phone 555-555-0184

```html
<!DOCTYPE html>
<html lang="en">
<head>
<meta charset="utf-8">
<title>Harlow Wealth Management – Stationery</title>
<link href="https://fonts.googleapis.com/css2?family=Open+Sans:wght@400;600;700&display=swap" rel="stylesheet">
<style>
  :root{
    --bg:#ececec;
    --paper:#ffffff;
    --blue:#3d6a9a;
    --sage:#95ab90;
    --ink:#4a4a4a;
    --muted:#7a7a7a;
    --band:#e6e8e5;
    --signature:#dcdcdc;
  }
  *{margin:0;padding:0;box-sizing:border-box}
  html,body{width:1200px;height:795px;overflow:hidden}
  body{background:var(--bg);font-family:"Open Sans",Arial,sans-serif;color:var(--ink);position:relative}

  .letterhead{position:absolute;left:60px;top:26px;width:524px;height:742px;background:var(--paper);box-shadow:0 2px 10px rgba(0,0,0,.08);padding:44px 54px 0 54px}
  .brand{display:flex;align-items:center;gap:12px}
  .brand-mark{width:46px;height:46px;border-radius:50%;background:var(--sage);flex:none}
  .brand-name{font-weight:700;font-size:17px;color:var(--blue);letter-spacing:.5px;text-transform:uppercase;line-height:1.15}
  .letter-body{margin-top:40px;font-size:8.6px;line-height:1.55;color:var(--ink);padding-left:24px}
  .letter-body .salutation{font-weight:700;margin-bottom:8px}
  .letter-body p{margin-bottom:9px}
  .signature{margin-top:22px;padding-left:24px}
  .signature-art{width:110px;height:26px;background:var(--signature);border-radius:3px}
  .signature-role{font-size:8.6px;font-weight:700;margin-top:4px}

  .letter-footer{position:absolute;left:0;right:0;bottom:0;height:70px}
  .footer-band{position:absolute;bottom:0;height:70px;width:30px;background:var(--band)}
  .footer-band.left{left:0}
  .footer-band.right{right:0}
  .footer-rule{position:absolute;left:54px;right:54px;top:14px;height:1px;background:var(--blue)}
  .footer-info{position:absolute;left:54px;right:54px;top:22px;display:flex;justify-content:space-between;font-size:7.5px;line-height:1.6;color:var(--muted)}
  .label{color:var(--blue);margin-right:4px}
  .web{color:var(--blue)}

  .card{position:absolute;top:190px;width:230px;height:402px;background:var(--paper);box-shadow:0 2px 10px rgba(0,0,0,.08)}
  .card-front{left:660px;display:flex;flex-direction:column}
  .card-band{height:100px;background:var(--band)}
  .card-center{flex:1;display:flex;flex-direction:column;align-items:center;justify-content:center;gap:12px}
  .card-front .brand-mark{width:76px;height:76px}
  .card-front .brand-name{font-size:15px;text-align:center}

  .card-back{left:920px;padding:40px 26px}
  .card-back .brand-mark{display:block;width:66px;height:66px;margin:0 auto}
  .person{margin-top:34px}
  .card-rule{height:1px;background:var(--blue)}
  .person-name{font-size:13px;color:var(--blue);padding:6px 0 4px}
  .person-title{font-size:8px;color:var(--muted);padding:4px 0 6px}
  .card-contact{margin-top:14px;font-size:8px;line-height:1.6;color:var(--muted)}
  .card-contact .address{margin-top:10px}
  .card-contact .web{margin-top:10px;display:block}
</style>
</head>
<body>

<section class="letterhead">
  <header class="brand">
    <span class="brand-mark"></span>
    <span class="brand-name">Harlow Wealth Management</span>
  </header>

  <div class="letter-body">
    <p class="salutation">Lorem Ipsum,</p>
    <p>Cras mattis consectetur purus sit amet fermentum. Etiam porta sem malesuada magna mollis euismod. Integer posuere erat a ante venenatis dapibus posuere velit aliquet. Cras justo odio, dapibus ac facilisis in, egestas eget quam. Aenean eu leo quam. Pellentesque ornare sem lacinia quam venenatis vestibulum.</p>
    <p>Vivamus sagittis lacus vel augue laoreet rutrum faucibus dolor auctor. Donec sed odio dui. Etiam porta sem malesuada magna mollis euismod. Morbi leo risus, porta ac consectetur ac, vestibulum at eros. Nullam id dolor id nibh ultricies vehicula ut id elit.</p>
    <p>Donec id elit non mi porta gravida at eget metus. Fusce dapibus, tellus ac cursus commodo, tortor mauris condimentum nibh, ut fermentum massa justo sit amet risus. Cras justo odio, dapibus ac facilisis in, egestas eget quam. Cum sociis natoque penatibus et magnis dis parturient montes, nascetur ridiculus mus.</p>
    <p>Cum sociis natoque penatibus et magnis dis parturient montes, nascetur ridiculus mus. Curabitur blandit tempus porttitor. Aenean lacinia bibendum nulla sed consectetur. Lorem ipsum dolor sit amet, consectetur adipiscing elit.</p>
    <p>Cras justo odio, dapibus ac facilisis in, egestas eget quam. Morbi leo risus, porta ac consectetur ac, vestibulum at eros. Duis mollis, est non commodo luctus, nisi erat porttitor ligula, eget lacinia odio sem nec elit. Integer posuere erat a ante venenatis dapibus posuere velit aliquet. Vivamus sagittis lacus vel augue laoreet rutrum faucibus dolor auctor.</p>
  </div>

  <div class="signature">
    <div class="signature-art" role="img" aria-label="Handwritten signature"></div>
    <div class="signature-role">Company Director</div>
  </div>

  <footer class="letter-footer">
    <div class="footer-band left" role="img" aria-label="Fine diagonal stripe pattern in light grey"></div>
    <div class="footer-band right" role="img" aria-label="Fine diagonal stripe pattern in light grey"></div>
    <div class="footer-rule"></div>
    <div class="footer-info">
      <div><span class="label">T</span>555-555-0184<br><span class="label">E</span>ray@harlowwealthmgmt.example</div>
      <div>4820 Bramblewood Lane,<br>Suite 317 Linden Bay, 00000</div>
      <div class="web">harlowwealthmgmt.example</div>
    </div>
  </footer>
</section>

<section class="card card-front">
  <div class="card-band" role="img" aria-label="Fine diagonal stripe pattern in light grey"></div>
  <div class="card-center">
    <span class="brand-mark"></span>
    <span class="brand-name">Harlow Wealth<br>Management</span>
  </div>
  <div class="card-band" role="img" aria-label="Fine diagonal stripe pattern in light grey"></div>
</section>

<section class="card card-back">
  <span class="brand-mark"></span>
  <div class="person">
    <div class="card-rule"></div>
    <div class="person-name">Raymond Kessler, MS, CFP</div>
    <div class="person-title">President Harlow Wealth Management</div>
    <div class="card-rule"></div>
  </div>
  <div class="card-contact">
    <div><span class="label">T</span>555-555-0184</div>
    <div><span class="label">E</span>ray@harlowwealthmgmt.example</div>
    <div class="address">4820 Bramblewood Lane,<br>Suite 317 Linden Bay, 00000</div>
    <span class="web">harlowwealthmgmt.example</span>
  </div>
</section>

</body>
</html>
```